Verlune Magician

I want the business card for my business to give to people who watch that later I will be employed to show magic here is my website http://www.verlunemagicien-exemple.fr/I want the interesting design , i am very opened for formal and informal, I watch a lot of design so don't stick to the common shape and form but i hope it can also be produced the thing to write on will be the same as in picture that i will upload , i also will upload the logo for you that so can be easy to useDenis CostilleMagicianMAGICIAN VERLUNE 17 rue des Tilleuls - 25000 BESANÇON contact@verlunemagicien-exemple.fr tel. 0381 476 093 tel. 0664 219 570

```html
<!DOCTYPE html>
<html lang="fr">
<head>
<meta charset="utf-8">
<title>Lucien Marbec – Carte de visite</title>
<link href="https://fonts.googleapis.com/css2?family=Questrial&display=swap" rel="stylesheet">
<style>
  :root {
    --backdrop: #2a2a2a;
    --card: #ffffff;
    --ink: #111111;
    --rule: #3a3a3a;
    --figure-dark: #0b0b0b;
    --figure-mid: #2e2e2e;
  }
  * { margin: 0; padding: 0; box-sizing: border-box; }
  html, body {
    width: 1200px;
    height: 900px;
    overflow: hidden;
    background: var(--backdrop);
  }
  .canvas {
    width: 1200px;
    height: 900px;
    display: flex;
    align-items: center;
    justify-content: center;
  }
  .business-card {
    position: relative;
    width: 1000px;
    height: 640px;
    background: var(--card);
    font-family: "Questrial", "Century Gothic", sans-serif;
    color: var(--ink);
    box-shadow: 0 24px 60px rgba(0,0,0,0.5);
    overflow: hidden;
  }
  .identity {
    position: absolute;
    left: 64px;
    top: 70px;
    width: 520px;
  }
  .identity__name {
    font-size: 54px;
    font-weight: 400;
    letter-spacing: 2px;
    text-transform: uppercase;
    line-height: 1;
    white-space: nowrap;
  }
  .identity__role {
    font-size: 22px;
    letter-spacing: 1px;
    text-transform: uppercase;
    margin-top: 8px;
  }
  .identity__rule {
    width: 110px;
    height: 2px;
    background: var(--rule);
    margin: 20px 0 24px;
  }
  .contact-list {
    list-style: none;
    font-size: 24px;
    line-height: 1.55;
    white-space: nowrap;
  }
  .artwork {
    position: absolute;
    left: 600px;
    top: 210px;
    width: 320px;
    height: 300px;
  }
  .brand-name {
    position: absolute;
    left: 560px;
    top: 530px;
    font-size: 68px;
    font-weight: 400;
    letter-spacing: 8px;
    color: var(--ink);
    line-height: 1;
    white-space: nowrap;
  }
</style>
</head>
<body>
<main class="canvas">
  <article class="business-card">
    <section class="identity">
      <h1 class="identity__name">Lucien Marbec</h1>
      <p class="identity__role">Magicien</p>
      <div class="identity__rule"></div>
      <ul class="contact-list">
        <li>0381 476 093 | 0664 219 570</li>
        <li>contact@verlunemagicien-exemple.fr</li>
        <li>www.verlunemagicien-exemple.fr</li>
        <li>17 rue des Tilleuls - 25000 BESANÇON</li>
      </ul>
    </section>

    <svg class="artwork" viewBox="0 0 320 300" role="img" aria-label="Black ink illustration of the magician in a dark jacket holding up a playing card">
      <defs>
        <linearGradient id="figure-tone" x1="0" y1="0" x2="0" y2="1">
          <stop offset="0" stop-color="var(--figure-mid)"/>
          <stop offset="1" stop-color="var(--figure-dark)"/>
        </linearGradient>
      </defs>
      <rect x="0" y="0" width="320" height="300" fill="url(#figure-tone)"/>
    </svg>

    <p class="brand-name">VERLUNE</p>
  </article>
</main>
</body>
</html>
```